Business Card Design

I am starting my therapy private practice. I will be an in home therapist, so I go into family's homes instead of using an office to do family/marriage therapy. Therefore, I do not have an office address. I am looking for something in the black, red, gray, and blue color scheme that appeals to both families, couples and teenagers.

Industry/Entity Type

Business

Contact Information for Business Card

Lena Brightwell, MS, MFT Intern
Marriage and Family Therapy
In Home Therapist
617-482-5190
Lena@LenaBrightwell-example.com

```html
<!DOCTYPE html>
<html lang="en">
<head>
<meta charset="utf-8">
<title>Lena Brightwell – Business Card</title>
<link rel="stylesheet" href="https://fonts.googleapis.com/css2?family=Tinos&family=Arimo:wght@400&display=swap">
<style>
  :root {
    --card-bg: #2e2e2e;
    --card-bg-edge: #1f1f1f;
    --emblem-light: #8a8a8a;
    --emblem-dark: #3a3a3a;
    --name-white: #ffffff;
    --subtitle-gray: #c9c9c9;
    --panel-bg: #353535;
    --divider-dots: #e6e6e6;
    --icon-red: #c8171c;
    --icon-red-dark: #9c0f13;
    --contact-text: #d6d6d6;
  }
  html, body {
    margin: 0;
    padding: 0;
    width: 1200px;
    height: 686px;
    overflow: hidden;
    background: var(--card-bg-edge);
  }
  .card {
    position: relative;
    width: 1200px;
    height: 686px;
    overflow: hidden;
    background: radial-gradient(ellipse at 40% 45%, var(--card-bg) 0%, #292929 60%, var(--card-bg-edge) 100%);
  }
  .emblem-area {
    position: absolute;
    left: 55px;
    top: 25px;
    width: 500px;
    height: 620px;
    border-radius: 50%;
    background: radial-gradient(ellipse at 55% 40%, rgba(138,138,138,0.45) 0%, rgba(110,110,110,0.25) 45%, rgba(58,58,58,0) 72%);
  }
  .identity {
    position: absolute;
    left: 146px;
    top: 318px;
  }
  .identity__name {
    margin: 0;
    font-family: "Tinos", "Times New Roman", serif;
    font-weight: 400;
    font-size: 64px;
    line-height: 1;
    color: var(--name-white);
    letter-spacing: 0.5px;
  }
  .identity__title {
    margin: 10px 0 0 22px;
    font-family: "Arimo", Arial, sans-serif;
    font-size: 22px;
    line-height: 33px;
    color: var(--subtitle-gray);
  }
  .divider {
    position: absolute;
    left: 640px;
    top: 298px;
    width: 0;
    height: 184px;
    border-left: 4px dotted var(--divider-dots);
  }
  .contact-panel {
    position: absolute;
    left: 662px;
    top: 303px;
    width: 538px;
    height: 173px;
    background: var(--panel-bg);
  }
  .contact-list {
    list-style: none;
    margin: 0;
    padding: 14px 0 0 36px;
  }
  .contact-item {
    display: flex;
    align-items: center;
    height: 70px;
    margin-bottom: 7px;
  }
  .contact-icon {
    width: 68px;
    height: 68px;
    flex: none;
  }
  .contact-text {
    margin-left: 14px;
    font-family: "Arimo", Arial, sans-serif;
    font-size: 27px;
    color: var(--contact-text);
  }
</style>
</head>
<body>
<main class="card">
  <div class="emblem-area" role="img" aria-label="Gray swirl emblem with leaves and an open hand"></div>

  <section class="identity">
    <h1 class="identity__name">Lena Brightwell</h1>
    <p class="identity__title">MS, MFT Intern Marriage and<br>Family Therapy In Home Therapist</p>
  </section>

  <div class="divider"></div>

  <section class="contact-panel">
    <ul class="contact-list">
      <li class="contact-item">
        <svg class="contact-icon" viewBox="0 0 68 68" aria-hidden="true">
          <defs>
            <linearGradient id="iconRed" x1="0" y1="0" x2="0" y2="1">
              <stop offset="0" stop-color="var(--icon-red)"/>
              <stop offset="1" stop-color="var(--icon-red-dark)"/>
            </linearGradient>
          </defs>
          <rect x="1" y="1" width="66" height="66" rx="8" fill="url(#iconRed)"/>
          <path d="M14 26 C14 16 54 16 54 26 L54 30 L44 30 L44 25 L24 25 L24 30 L14 30 Z" fill="#fff"/>
          <path d="M22 33 L46 33 L52 52 L16 52 Z" fill="#fff"/>
          <circle cx="34" cy="42" r="6" fill="var(--icon-red)"/>
          <circle cx="34" cy="42" r="2.5" fill="#fff"/>
        </svg>
        <span class="contact-text">617-482-5190</span>
      </li>
      <li class="contact-item">
        <svg class="contact-icon" viewBox="0 0 68 68" aria-hidden="true">
          <rect x="1" y="1" width="66" height="66" rx="8" fill="url(#iconRed)"/>
          <rect x="13" y="20" width="42" height="28" fill="#fff"/>
          <path d="M13 20 L34 37 L55 20" fill="none" stroke="var(--icon-red)" stroke-width="3"/>
          <path d="M13 48 L28 33 M55 48 L40 33" fill="none" stroke="var(--icon-red)" stroke-width="2"/>
        </svg>
        <span class="contact-text">Lena@LenaBrightwell-example.com</span>
      </li>
    </ul>
  </section>
</main>
</body>
</html>
```